New online business - used mobile phones - needs unique eye catching web design that sets it apart

The Handset Bazaar
We are a new business looking for a rapid response for our web site design. We don't want a normal website....... we need to be creative - most important PLEASE view the attached files uploaded 3 March to ensure you get us :)
.
The Handset Bazaar buys new and damaged mobile phones from the public. A simple process they complete to sell their mobile to us; we want our website to reflect this.
Our website needs to be modern, edgy and fun, not corporate and definitely not like any other mobile phone buying site in the world today!!
Our name was taken from a play on the share/stock market which we have tried to bring into the design ....... it hasn't worked with early designs submitted. Now taking a different approach. Refer to new attached files which should help you visualise our concept.

We like layout from Artisan Hive – plvendrake #7318290 design as this is very close to our layout vision.
The first page to tell the public what we do, how we do it, and then they click to accept the instant online quote. (page two they complete details about the mobiles model & condition they are selling, then page three complete their personal details).
Our background preference is dark, blackboard or dark with slight texture
a) We love white on black/dark background either typewriter font or look like hand drawn refer to attached files & quillandfennel.com.au site to see. Would Label font work???

b) Where the light blue colour is on #7318290 this needs to be like chromadex colour classic green, fern green or bright green, not fluorescent lime green or an insipid green.

c) The banner says The Handset Bazaar is open........... for buying mobiles for cash $$$ (we need people to know we BUY used/damaged phones)

d) We love colour either solid colour or looks like it has been coloured in on our dark background. Open to white or pastel background versions refer to attached coffee file.
We like Chromadex Orange 021,Haute Red,Dazzling Blue, Cyan Blue, Beetroot Purple, Island Green.
e) How it works – underneath this title put Our deal …………. It’s easy as…………..quote, post, get paid!!!
Quote – first circle hand drawn icon showing mobile phone & $ sign. Underneath it says .....Obtain Quote for Model & Condition
Post – second circle hand drawn icon show parcel. Underneath it says Free Post
Paid – third circle hand drawn icon showing large $ sign. Underneath it says Payment in Two Days
Plans - is swapped for wording- Get Market Quote with a large button which says GO or CLICK HERE (they click on the button & it takes them to the next page)
f) FAQ
Allow for six FAQ’s we will forward correct content to you for final design layout.

g) About Us
Please allow about a paragraph of text here, we will forward correct content to you for final design layout.
h) Contact Us
At the bottom where normal website have ………. home, contact details, blog, etc, please only put Email us & Call us, then social media icons for FB, Linked In and Twitter

I) LOGO We don’t have one yet, just put The Handset Bazaar at the top & it needs to be large sized font ................we are new and we need to push our name
If you are not clear on our vision ..........please email me and I will reply very quickly.
Thank you for taking the time to read & understand & get us:)

Target Market(s)

20-45 years any body with a spare smart phone that is lying around and they can get cash for. Target market could be slightly older to 50 but focus of 20-40's

Industry/Entity Type

Business

Number of Pages Required

3 page

Font styles to use
Other font styles liked:
• handwritten font or typewriter font

Requirements
Must have
• Read only attached files dated 4 March, tech error with other files, being removed.
• 1 Layout design of Artisan Hive – plvendrake #7318290
• 2 Hand drawn icons - refer to files
• 3 White font needs to look like hand written refer to quillandfennel.com.au or typewriter font - large size font
• 4 Main colours are Black or dark background, green with white text, preference is hand drawn font. The three circles for quote, post & pay with hand drawn icons can be any colour ...... Purple for quote, orange for post & green for paid
• 5 Big green button underneath 3 circles quote/post/pay - customers click on big button to get instant quote
Nice to have
• Coloured in hand drawings as per file
• Great Hand drawings coloured in
Should not have
• NO template designs so it look like you just put some text & a photo. Don't fill the page with mobile phones, one or two is ok, mobile phone pictures date so fast.
• Cartoons

```html
<!DOCTYPE html>
<html lang="en">
<head>
<meta charset="utf-8">
<title>The Handset Bazaar</title>
<link href="https://fonts.googleapis.com/css2?family=Covered+By+Your+Grace&family=Montserrat:wght@300;400;500&display=swap" rel="stylesheet">
<style>
:root{
  --green:#14924f;
  --green-dark:#0f7a41;
  --ink:#1d1d1d;
  --grey-text:#555;
  --band:#e0e0e0;
  --white:#fff;
  --rule:#c9c9c9;
}
*{box-sizing:border-box;margin:0;padding:0}
html,body{width:1200px;height:2429px;overflow:hidden}
body{position:relative;background:var(--white);font-family:"Montserrat",Arial,sans-serif;color:var(--ink)}
.abs{position:absolute}
.script{font-family:"Covered By Your Grace",cursive}

/* header */
.site-header{left:0;top:0;width:1200px;height:93px;background:linear-gradient(#3a3a3a,#050505)}
.brand{left:49px;top:18px;width:170px;color:var(--white);font-size:17px;font-weight:500;line-height:22px;text-align:center}
.nav{left:380px;top:0;height:73px;display:flex;font-size:12px;color:var(--white);letter-spacing:.3px}
.nav a{display:block;line-height:73px;padding:0 14px;color:inherit;text-decoration:none}
.nav a.active{background:var(--green);width:57px;padding:0;text-align:center}
.nav .gap{width:14px}
.header-social{left:1080px;top:32px;display:flex;gap:15px}
.header-social span{width:13px;height:13px;border-radius:50%;background:#8a8a8a}

/* hero */
.hero{left:0;top:93px;width:1200px;height:587px;background:radial-gradient(ellipse at 55% 45%,#2ba868 0%,#1a9658 45%,#0e7d45 100%)}
.hero-title{left:0;top:290px;width:1200px;text-align:center;color:var(--white);font-size:78px;line-height:82px}
.dots{left:555px;top:619px;display:flex;gap:13px}
.dots span{width:7px;height:7px;border-radius:50%;background:rgba(255,255,255,.55)}
.dots span:first-child{background:var(--white)}

/* section titles */
.section-title{left:0;width:1200px;text-align:center;font-size:36px;color:var(--ink);line-height:40px}
.rule{top:748px;height:1px;background:var(--rule)}
.lede{left:0;top:778px;width:1200px;text-align:center;font-size:19px;font-weight:300;color:var(--grey-text)}

/* steps */
.step-ring{width:178px;height:178px;border-radius:50%;border:6px solid var(--green);background:var(--white);display:flex;align-items:center;justify-content:center}
.step-art{width:120px;height:120px;border-radius:50%;background:radial-gradient(#f2f2f2,#dcdcdc)}
.step-label{width:300px;text-align:center;color:var(--green);font-size:27px;line-height:34px}

/* bands */
.band{left:0;width:1200px;background:var(--band)}
.copy{left:235px;width:830px;text-align:center;font-size:15.5px;font-weight:300;line-height:20px;color:#333}
.cta{left:458px;top:1430px;width:282px;height:44px;background:var(--green);color:var(--white);font-size:16px;line-height:44px;text-align:center}

/* faq */
.faq{left:213px;width:860px}
.faq-item{display:flex;align-items:center;gap:10px;font-size:15.5px;font-weight:500;height:24px}
.faq-item svg{flex:none}
.faq-item.open{color:var(--green)}
.faq-answer{padding-left:27px;font-size:12.5px;font-weight:300;line-height:16px;color:#333;margin:6px 0 0}

/* footer */
.site-footer{left:0;top:2281px;width:1200px;height:148px;background:var(--green);color:var(--white);font-size:14px;line-height:22.5px}
.foot-col{display:flex;gap:10px}
.foot-social{left:657px;top:2326px;display:flex;gap:22px;align-items:center}
.foot-social span{width:24px;height:24px;border-radius:4px;background:var(--white)}
.copyright{right:47px;top:2314px;font-size:13.5px}
.foot-brand{left:1000px;top:2352px;width:155px;text-align:center;font-size:17px;font-weight:500;line-height:21px}
</style>
</head>
<body>

<header class="site-header abs">
  <div class="brand abs">The<br>Handset Bazaar</div>
  <nav class="nav abs">
    <a class="active" href="#">HOME</a><span class="gap"></span>
    <a href="#">ABOUT US</a>
    <a href="#">HOW IT WORKS</a>
    <a href="#">PLANS</a>
    <a href="#">FAQ</a>
    <a href="#">CONTACT</a>
  </nav>
  <div class="header-social abs"><span></span><span></span><span></span></div>
</header>

<section class="hero abs" role="img" aria-label="Green-tinted photo of a hand holding a smartphone"></section>
<h1 class="hero-title abs script">The Handset Bazaar is open for<br>buying mobiles for cash</h1>
<div class="dots abs"><span></span><span></span><span></span><span></span><span></span></div>

<!-- how it works -->
<div class="rule abs" style="left:49px;width:440px"></div>
<div class="rule abs" style="left:711px;width:442px"></div>
<h2 class="section-title abs script" style="top:726px">How it Works</h2>
<p class="lede abs">Our deal .......... It’s easy as..........quote, post, get paid!!!</p>

<div class="step-ring abs" style="left:227px;top:860px"><div class="step-art" role="img" aria-label="Hand-drawn phone with a dollar sign"></div></div>
<div class="step-ring abs" style="left:527px;top:860px"><div class="step-art" role="img" aria-label="Hand-drawn parcel"></div></div>
<div class="step-ring abs" style="left:813px;top:860px"><div class="step-art" role="img" aria-label="Hand-drawn large dollar sign"></div></div>

<p class="step-label abs script" style="left:166px;top:1056px">Obtain quote for<br>model &amp; condition</p>
<p class="step-label abs script" style="left:466px;top:1056px">Free post</p>
<p class="step-label abs script" style="left:752px;top:1056px">Payment into your bank<br>account within two days</p>

<!-- plans -->
<section class="band abs" style="top:1166px;height:358px"></section>
<h2 class="section-title abs script" style="top:1203px">Plans</h2>
<p class="copy abs" style="top:1275px">Praesent vestibulum aenean nonummy hendrerit mauris. Cum sociis natoque penatibus et mgnis dis parturient mntes ascetur ridiculus mus. Nullaa dui. Fusce feugiat malesuada odio orbi nunc odio gravida at cursus nec luctus a lorem.Praesent vestibulum aenean nonummy hendrerit mauris. Cum sociis natoque penatibus et mgnis dis parturient mntes ascetur ridiculus mus. Nullaa dui.</p>
<p class="copy abs" style="top:1375px">Fusce feugiat malesuada odio orbi nunc odiogravida at cursus nec luctus a lorem.</p>
<a class="cta abs" href="#">Get Market Quote</a>

<!-- faq -->
<h2 class="section-title abs script" style="top:1562px">Faq’s</h2>
<div class="faq abs" style="top:1648px">
  <div class="faq-item open"><svg width="15" height="15" viewBox="0 0 16 16"><circle cx="8" cy="8" r="8" fill="#14924f"/><path d="M4.5 6.5 8 10l3.5-3.5" stroke="#fff" stroke-width="2" fill="none"/></svg>Praesent vestibulum aenean nonummy hendrerit mauris. Cum sociis natoque penatibus etmntes</div>
  <p class="faq-answer">Cum sociis natoque penatibus et mgnis dis parturientmntes ascetur ridiculus mus. Nulladui. Fusce feugiat malesuada odio orbi nunc odio gravida at cursusnec luctus a lorem.Cum sociis natoque penatibus et mgnis dis parturient</p>
</div>
<div class="faq abs" style="top:1732px">
  <div class="faq-item" style="margin-bottom:14px"><svg width="15" height="15" viewBox="0 0 16 16"><circle cx="8" cy="8" r="8" fill="#1d1d1d"/><path d="M6.5 4.5 10 8l-3.5 3.5" stroke="#fff" stroke-width="2" fill="none"/></svg>Praesent vestibulum aenean nonummy hendrerit mauris. Cum sociis natoque penatibus etmntes</div>
  <div class="faq-item" style="margin-bottom:14px"><svg width="15" height="15" viewBox="0 0 16 16"><circle cx="8" cy="8" r="8" fill="#1d1d1d"/><path d="M6.5 4.5 10 8l-3.5 3.5" stroke="#fff" stroke-width="2" fill="none"/></svg>Praesent vestibulum aenean nonummy hendrerit mauris.</div>
  <div class="faq-item" style="margin-bottom:14px"><svg width="15" height="15" viewBox="0 0 16 16"><circle cx="8" cy="8" r="8" fill="#1d1d1d"/><path d="M6.5 4.5 10 8l-3.5 3.5" stroke="#fff" stroke-width="2" fill="none"/></svg>Praesent vestibulum aenean nonummy hendrerit mauris. Cum sociis natoque penatibus etmntes</div>
  <div class="faq-item" style="margin-bottom:14px"><svg width="15" height="15" viewBox="0 0 16 16"><circle cx="8" cy="8" r="8" fill="#1d1d1d"/><path d="M6.5 4.5 10 8l-3.5 3.5" stroke="#fff" stroke-width="2" fill="none"/></svg>Praesent vestibulum aenean nonummy hendrerit mauris.</div>
  <div class="faq-item" style="margin-bottom:14px"><svg width="15" height="15" viewBox="0 0 16 16"><circle cx="8" cy="8" r="8" fill="#1d1d1d"/><path d="M6.5 4.5 10 8l-3.5 3.5" stroke="#fff" stroke-width="2" fill="none"/></svg>Praesent vestibulum aenean nonummy hendrerit mauris. Cum sociis natoque penatibus etmntes</div>
  <div class="faq-item"><svg width="15" height="15" viewBox="0 0 16 16"><circle cx="8" cy="8" r="8" fill="#1d1d1d"/><path d="M6.5 4.5 10 8l-3.5 3.5" stroke="#fff" stroke-width="2" fill="none"/></svg>Praesent vestibulum aenean nonummy hendrerit mauris.</div>
</div>

<!-- about -->
<section class="band abs" style="top:2008px;height:273px"></section>
<h2 class="section-title abs script" style="top:2045px">About Us</h2>
<p class="copy abs" style="top:2117px">Praesent vestibulum aenean nonummy hendrerit mauris. Cum sociis natoque penatibus et mgnis dis parturient mntes ascetur ridiculus mus. Nullaa dui. Fusce feugiat malesuada odio orbi nunc odio gravida at cursus nec luctus a lorem.Praesent vestibulum aenean nonummy hendrerit mauris. Cum sociis natoque penatibus et mgnis dis parturient mntes ascetur ridiculus mus. Nullaa dui.</p>
<p class="copy abs" style="top:2216px">Fusce feugiat malesuada odio orbi nunc odiogravida at cursus nec luctus a lorem.</p>

<!-- footer -->
<footer class="site-footer abs"></footer>
<div class="foot-col abs" style="left:52px;top:2316px;color:#fff;font-size:14px;line-height:22.5px">
  <svg width="11" height="15" viewBox="0 0 12 16" style="margin-top:4px"><path d="M6 0a6 6 0 0 0-6 6c0 4.5 6 10 6 10s6-5.5 6-10a6 6 0 0 0-6-6z" fill="#fff"/><circle cx="6" cy="6" r="2.2" fill="#14924f"/></svg>
  <div>Address line here and<br>address line fully texted<br>Addres pincode, country</div>
</div>
<div class="abs" style="left:318px;top:2317px;color:#fff;font-size:14px;line-height:22.5px">
  <div class="foot-col"><svg width="13" height="13" viewBox="0 0 16 16" style="margin-top:4px"><path d="M3.6 1 6 3.8 4.7 5.6c.9 2 2.6 3.7 4.7 4.7L11.2 9 14 11.4 12.6 14C7 14 2 9 2 3.4z" fill="#fff"/></svg><span>44 712 4038 2261</span></div>
  <div class="foot-col"><svg width="13" height="13" viewBox="0 0 16 16" style="margin-top:5px"><rect x="1" y="3" width="14" height="10" fill="#fff"/><path d="M1 3l7 6 7-6" stroke="#14924f" stroke-width="1.4" fill="none"/></svg><span>hello@handsetbazaar.example</span></div>
</div>
<div class="foot-social abs"><span></span><span></span><span></span></div>
<p class="copyright abs" style="color:#fff">All rights reserved. Copyrights @ 2015</p>
<div class="foot-brand abs" style="color:#fff">The<br>Handset Bazaar</div>

</body>
</html>
```